Business Card Design Project for Web Development Company

Need a professional card that stands out with both color and texture.
We provide websites and web development services for small businesses with a focus on connections. Examples include: Automotive repair shop, we take their repair logs and make them available online so their customers can view, print and share (when selling) their maintenance records. Vet clinic, we create systems where customers can sign up for a recurring payment program for the annual wellness checks on their pets and get reminders when it's time, then see and schedule their own appointments. Etc... So not simply a website, but one that connects systems or customers to the business.
Important - !!!!We will be using http://inkvaleprinters.com/ for the cards, so take a look at what options are available for business card printing, they can do a lot of cool things!!!!
You can pick any 1-3 options from inkvaleprinters. I'm leaning towards a black background, but the logo will work on any color.
Front:
Marcus Telford
2750 SW 8th Ave STE 214-587
Alder Falls, OR 97799
541-617-2038 - cell
541-259-7306 - office
marcus@sitelinkhub.com
www.SiteLinkHub.com
Updates
We provide websites and web development services for small businesses with a focus on connections. Examples include: Automotive repair shop, we take their repair logs and make them available online so their customers can view, print and share (when selling) their maintenance records. Vet clinic, we create systems where customers can sign up for a recurring payment program for the annual wellness checks on their pets and get reminders when it''s time, then see and schedule their own appointments. Etc... So not simply a website, but one that connects systems or customers to the business.
Target Market(s)
Small business owners
Industry/Entity Type
Automotive
Look and feel
Each slider illustrates characteristics of the customer's brand and the style your logo design should communicate.

```html
<!DOCTYPE html>
<html lang="en">
<head>
<meta charset="utf-8">
<title>SiteLinkHub Business Card</title>
<link rel="stylesheet" href="https://fonts.googleapis.com/css2?family=Source+Sans+3:wght@400;600&display=swap">
<style>
  :root {
    --page-bg: #2b2b2d;
    --card-dark: #3a4247;
    --band-dark: #353e43;
    --silver-light: #eef0f1;
    --silver-mid: #d3d6d8;
    --silver-deep: #bfc3c6;
    --brand-blue: #1b8fd4;
    --ink: #3a3f43;
    --paper-white: #f2f4f6;
  }
  * { box-sizing: border-box; margin: 0; padding: 0; }
  html, body { width: 1200px; height: 900px; overflow: hidden; }
  body {
    background: var(--page-bg);
    font-family: "Source Sans 3", sans-serif;
    position: relative;
  }
  .card {
    position: absolute;
    top: 295px;
    width: 494px;
    height: 310px;
    border-radius: 22px;
    overflow: hidden;
  }
  .card--back {
    left: 94px;
    background: var(--card-dark);
  }
  .card--front {
    left: 615px;
    background: linear-gradient(135deg, var(--silver-light) 0%, var(--silver-mid) 45%, var(--silver-light) 70%, var(--silver-deep) 100%);
  }
  .brand {
    display: flex;
    align-items: center;
    gap: 10px;
    font-weight: 600;
    color: var(--paper-white);
    letter-spacing: 0.5px;
  }
  .brand__dot {
    width: 14px; height: 14px;
    border-radius: 50%;
    background: var(--brand-blue);
  }
  .card--back .brand {
    position: absolute;
    left: 0; right: 0;
    top: 128px;
    justify-content: center;
    font-size: 46px;
  }
  .card--back .website {
    position: absolute;
    left: 0; right: 0;
    bottom: 24px;
    text-align: center;
    color: var(--paper-white);
    font-size: 15px;
  }
  .brand-band {
    position: absolute;
    left: 0; right: 0;
    top: 34px;
    height: 48px;
    background: var(--band-dark);
  }
  .brand-band .brand {
    position: absolute;
    left: 76px; top: 0; bottom: 0;
    font-size: 44px;
  }
  .holder {
    position: absolute;
    left: 29px;
    top: 147px;
  }
  .holder__name {
    color: var(--brand-blue);
    font-size: 22px;
    letter-spacing: 0.5px;
    line-height: 1.1;
  }
  .holder__title {
    color: var(--ink);
    font-size: 18px;
    line-height: 1.25;
  }
  .contact {
    position: absolute;
    left: 29px;
    top: 220px;
    font-size: 13.5px;
    line-height: 21px;
    color: var(--ink);
  }
  .contact__row { display: flex; }
  .contact__label { color: var(--brand-blue); width: 44px; }
  .address {
    position: absolute;
    left: 273px;
    top: 220px;
    font-size: 13.5px;
    line-height: 21px;
    color: var(--ink);
  }
  .address__line { padding-left: 16px; position: relative; }
  .address__pin { position: absolute; left: 0; top: 3px; }
</style>
</head>
<body>
  <section class="card card--back">
    <div class="brand"><span class="brand__dot"></span>SiteLinkHub</div>
    <p class="website">www.SiteLinkHub.com</p>
  </section>

  <section class="card card--front">
    <div class="brand-band">
      <div class="brand"><span class="brand__dot"></span>SiteLinkHub</div>
    </div>
    <div class="holder">
      <p class="holder__name">MARCUS TELFORD</p>
      <p class="holder__title">Managing Director</p>
    </div>
    <div class="contact">
      <p class="contact__row"><span class="contact__label">Cell:</span>541-617-2038</p>
      <p class="contact__row"><span class="contact__label">Office:</span>541-259-7306</p>
      <p class="contact__row"><span class="contact__label">Email:</span>marcus@sitelinkhub.com</p>
    </div>
    <div class="address">
      <p class="address__line">
        <svg class="address__pin" width="11" height="15" viewBox="0 0 11 15" aria-hidden="true">
          <path d="M5.5 0C2.5 0 0 2.4 0 5.4 0 9.3 5.5 15 5.5 15S11 9.3 11 5.4C11 2.4 8.5 0 5.5 0z" fill="var(--brand-blue)"/>
          <circle cx="5.5" cy="5.4" r="2" fill="var(--silver-light)"/>
        </svg>
        2750 SW 8th Ave STE 214-587
      </p>
      <p class="address__line">Alder Falls, OR 97799</p>
    </div>
  </section>
</body>
</html>
```